Tidewell Shuck-new seafood raw bar restaurant menu

We are a Local Seafood & Raw Bar restaurant that is looking to open in 3 months. I need-Dinner Menu Design, Happy Hour Menu, Cocktail Menu, Brunch Menu, Lunch Menu. I'd like to have you start w/ the dinner menu first then whomever I choose will also do the rest of my menus. The OYSTERDECK by Finnhook menu is the direction im going for as far as font organization. Id like you to give us our own personal touch. Ive also provided a mock menu that a local designer started that can't finish due to timing.

Target Market(s)

mid to high end casual seafood restaurant

Industry/Entity Type

restaurant

Font styles to use
Serif
Sans Serif

Colors
0054AA
0677BA
7BADD7
CADEEF
E8F1F8
0094D4
00A9DD
6FCCEA
C7EBF8
E9F6FB
00AB8E
00BBA5
67D7C9
C6EFE9
E9F9F6

Requirements
Must have
• 11" x 14" size

```html
<!DOCTYPE html>
<html lang="en">
<head>
<meta charset="utf-8">
<title>Tidewell Shuck — Dinner Menu</title>
<link rel="stylesheet" href="https://fonts.googleapis.com/css2?family=Bebas+Neue&family=Roboto+Slab:wght@700;800&family=Source+Sans+3:wght@400;700&display=swap">
<style>
  :root{
    --ink:#0054AA;
    --ink-mid:#0677BA;
    --sky:#C7EBF8;
    --sky-pale:#E9F6FB;
    --sea:#00BBA5;
    --paper:#ffffff;
  }
  *{margin:0;padding:0;box-sizing:border-box}
  html,body{width:1200px;height:905px;overflow:hidden;background:var(--paper)}
  .menu{position:relative;width:1200px;height:905px;color:var(--ink);font-family:'Source Sans 3',sans-serif}
  .frame{position:absolute;left:23px;top:24px;width:1154px;height:851px;border:2.5px solid var(--ink-mid);border-radius:14px}
  .brand{position:absolute;left:49px;top:56px;display:flex;align-items:center;gap:12px}
  .brand-dot{width:34px;height:34px;border-radius:50%;background:var(--ink)}
  .brand-name{font:800 30px/1 'Roboto Slab',serif;letter-spacing:1px;text-transform:uppercase;color:var(--ink)}
  .heading{position:absolute;font:400 44px/1 'Bebas Neue',sans-serif;letter-spacing:.5px;color:var(--ink)}
  .item{position:absolute}
  .item .name{font:700 17px/18px 'Source Sans 3',sans-serif;text-transform:uppercase}
  .item .desc{font:400 13px/15.5px 'Source Sans 3',sans-serif}
  .item .price{position:absolute;right:0;top:0;font:700 12.5px/18px 'Source Sans 3',sans-serif}
  .col-left .item{left:49px;width:276px}
  .col-mid .item{left:436px;width:317px}
  .col-right .item{left:842px;width:276px}
  .col-left .item .desc,.col-right .item .desc,.col-mid .item .desc{white-space:nowrap}
  .rule{position:absolute;height:1.2px;background:var(--sea)}
  .rule.left{left:40px;width:319px}
  .rule.right{left:832px;width:319px}
  .soups{position:absolute;left:35px;top:596px;width:328px;height:242px;background:var(--sky-pale);border:1px solid var(--sky)}
  .soups-title{position:absolute;left:49px;top:604px;font:700 28px/1 'Roboto Slab',serif;text-transform:lowercase}
  .soups-title small{font-size:16px;font-style:normal}
  .rule.soup{left:49px;width:298px;background:var(--ink-mid)}
  .addon{position:absolute;left:172px;top:830px;width:189px;height:13px;border-radius:6px;background:var(--sky);font:700 7.5px/13px 'Roboto Slab',serif;text-align:center}
  .panel{position:absolute;left:422px;width:355px;background:var(--sky);border-radius:12px}
  .slab{position:absolute;font-family:'Roboto Slab',serif;font-weight:800;color:var(--ink)}
  .panel-title{font-size:29px;line-height:1;letter-spacing:1.5px;text-transform:uppercase}
  .row-label{font-size:18px;line-height:1}
  .row-price{font-size:12px;font-weight:700;line-height:1;text-align:center;width:40px}
  .col-head{position:absolute;text-align:center;width:60px;font:700 15px/1 'Roboto Slab',serif}
  .col-head span{display:block;font:400 10px/1.2 'Source Sans 3',sans-serif}
  .hline{position:absolute;left:442px;width:315px;height:1px;background:var(--ink-mid)}
  .vline{position:absolute;width:1px;background:var(--ink-mid)}
  .disclaimer{position:absolute;left:40px;top:855px;font:700 9px/1 'Roboto Slab',serif}
</style>
</head>
<body>
<main class="menu">
  <div class="frame"></div>

  <section class="col-left">
    <div class="brand"><span class="brand-dot"></span><span class="brand-name">Tidewell Shuck</span></div>
    <h2 class="heading" style="left:48px;top:141px">Sharables</h2>

    <div class="item" style="top:188px"><div class="name">Fried Shrimp</div><div class="desc">Remoulade</div><div class="price">00</div></div>
    <div class="rule left" style="top:231px"></div>
    <div class="item" style="top:237px"><div class="name">Mussels</div><div class="desc">Local bacon, shallot, garlic, tomato, spicy herb butter</div><div class="price">00</div></div>
    <div class="rule left" style="top:280px"></div>
    <div class="item" style="top:287px"><div class="name">Shrimp and Grits</div><div class="desc">Local andouille, roasted peppers, garlic,<br>shallot, charred tomato</div><div class="price">00</div></div>
    <div class="rule left" style="top:345px"></div>
    <div class="item" style="top:352px"><div class="name">Crab Mac’n Cheese</div><div class="desc">Cheddar, fontina, cotija, local pasta shells</div><div class="price">00</div></div>
    <div class="rule left" style="top:395px"></div>
    <div class="item" style="top:402px"><div class="name">Shrimp Remoulade</div><div class="desc">Avocado, fried green tomato</div><div class="price">00</div></div>
    <div class="rule left" style="top:446px"></div>
    <div class="item" style="top:452px"><div class="name">Pumpkin Risotto</div><div class="desc">Herbs, dried cherry, local mushrooms</div><div class="price">00</div></div>
    <div class="rule left" style="top:494px"></div>
    <div class="item" style="top:502px"><div class="name">Eggplant Napolean</div><div class="desc">red pepper, goat cheese, basil</div><div class="price">00</div></div>
    <div class="rule left" style="top:545px"></div>
    <div class="item" style="top:551px"><div class="name">Poke</div><div class="desc">soy, sesame, scallion</div><div class="price">00</div></div>

    <div class="soups"></div>
    <h2 class="soups-title">soups <small>and</small> salads</h2>
    <div class="item" style="top:640px"><div class="name">Caesar</div><div class="desc">Baby gem lettuce, parmesan</div><div class="price">00</div></div>
    <div class="rule soup" style="top:682px"></div>
    <div class="item" style="top:689px"><div class="name">Marsh Sprout Salad</div><div class="desc">Fig, goat cheese, pepitos, sour cherry vin</div><div class="price">00</div></div>
    <div class="rule soup" style="top:732px"></div>
    <div class="item" style="top:739px"><div class="name">Clam Chowder</div><div class="desc">New England style</div><div class="price">00</div></div>
    <div class="rule soup" style="top:780px"></div>
    <div class="item" style="top:788px"><div class="name">Shrimp Brisque</div><div class="desc">Parmesan, chive oil</div><div class="price">00</div></div>
    <div class="addon">ADD TO AND SALAD: SHRIMP +12 CHICKEN +9</div>
  </section>

  <section class="col-mid">
    <h2 class="heading" style="left:435px;top:48px">Pasta</h2>
    <div class="item" style="top:94px"><div class="name">Clam Linguini</div><div class="desc">Local Pasta a Bacon, peppers, butter</div><div class="price">00</div></div>
    <div class="item" style="top:135px"><div class="name">Vegetable Gnocchi</div><div class="desc">Veggies, basil, parmesan</div><div class="price">00</div></div>
    <div class="item" style="top:176px"><div class="name">Lobster Agnolotti</div><div class="desc">Local bacon, mascarpone, parmesan, and<br>mushroom agnolotti, Brown butter, brandy,<br>capers, peppers, crème fraiche chervil</div><div class="price">00</div></div>
    <div class="item" style="top:247px"><div class="name">Crab Fettuccine</div><div class="desc">Cream, sherry, parmesan, fontina, Jumbo Crab, Peas</div><div class="price">00</div></div>
    <div class="item" style="top:288px"><div class="name">Shrimp Pasta</div><div class="desc">Royal Red Shrimp, champagne, pastis,<br>a trilogy of peppers, garlic, spicy herbed butter,<br>textured cheeses</div><div class="price">00</div></div>

    <div class="panel" style="top:373px;height:136px"></div>
    <div class="slab panel-title" style="left:442px;top:386px;font-size:30px">Oysters</div>
    <div class="col-head" style="left:612px;top:389px">6<span>OYSTERS</span></div>
    <div class="col-head" style="left:690px;top:389px">12<span>OYSTERS</span></div>
    <div class="vline" style="left:684px;top:384px;height:113px"></div>
    <div class="hline" style="top:421px"></div>
    <div class="slab row-label" style="left:450px;top:432px">House</div>
    <div class="slab row-price" style="left:620px;top:436px">16</div>
    <div class="slab row-price" style="left:700px;top:436px">28</div>
    <div class="hline" style="top:458px"></div>
    <div class="slab row-label" style="left:450px;top:469px">Regional</div>
    <div class="slab row-price" style="left:620px;top:474px">18</div>
    <div class="slab row-price" style="left:700px;top:474px">30</div>

    <div class="panel" style="top:529px;height:175px"></div>
    <div class="slab panel-title" style="left:440px;top:543px">Seafood Tower</div>
    <div class="hline" style="top:577px"></div>
    <div class="slab row-label" style="left:450px;top:588px">Small</div>
    <div class="slab row-price" style="left:701px;top:592px">53</div>
    <div class="hline" style="top:614px"></div>
    <div class="slab row-label" style="left:450px;top:626px">Large</div>
    <div class="slab row-price" style="left:701px;top:630px">90</div>
    <div class="hline" style="top:655px"></div>
    <div class="slab row-label" style="left:450px;top:667px">Build your own</div>
    <div class="slab row-price" style="left:703px;top:671px">110</div>

    <div class="slab panel-title" style="left:425px;top:722px;font-size:28px">Grilled</div>
    <div class="slab row-label" style="left:448px;top:759px">Rockefeller</div>
    <div class="slab row-price" style="left:577px;top:763px">18</div>
    <div class="slab row-label" style="left:448px;top:785px">Bienville</div>
    <div class="slab row-price" style="left:577px;top:789px">18</div>
    <div class="slab row-label" style="left:448px;top:812px">Tidewell Special</div>
    <div class="slab row-price" style="left:577px;top:816px">18</div>
    <div class="vline" style="left:624px;top:722px;height:112px"></div>
    <div class="slab panel-title" style="left:642px;top:722px;font-size:28px">Crudos</div>
    <div class="slab row-label" style="left:655px;top:759px">Salmon</div>
    <div class="slab row-price" style="left:728px;top:763px">14</div>
    <div class="slab row-label" style="left:655px;top:785px">Tuna</div>
    <div class="slab row-price" style="left:728px;top:789px">18</div>
    <div class="slab row-label" style="left:655px;top:812px">Scallop</div>
    <div class="slab row-price" style="left:728px;top:816px">18</div>
  </section>

  <section class="col-right">
    <h2 class="heading" style="left:841px;top:48px">Signature</h2>
    <div class="item" style="top:94px"><div class="name">Crab Legs</div><div class="desc">Butter, cocktail, spicy remoulade</div><div class="price">00</div></div>
    <div class="item" style="top:135px"><div class="name">Lowcountry Boil</div><div class="desc">Shrimp, sausage, corn, potato</div><div class="price">00</div></div>
    <div class="item" style="top:176px"><div class="name">Crab Cakes</div><div class="price">00</div></div>

    <h2 class="heading" style="left:841px;top:214px">Entrees</h2>
    <div class="item" style="top:261px"><div class="name">Clam Linguini</div><div class="desc">Local Pasta a Bacndon, peppers, butter</div><div class="price">00</div></div>
    <div class="rule right" style="top:302px"></div>
    <div class="item" style="top:309px"><div class="name">Vegetable Gnocchi</div><div class="desc">Veggies, basil, parmesan</div><div class="price">00</div></div>
    <div class="rule right" style="top:352px"></div>
    <div class="item" style="top:359px"><div class="name">Pan Seared Scallops</div><div class="desc">veggies, Carolina gold rice</div><div class="price">00</div></div>
    <div class="rule right" style="top:398px"></div>
    <div class="item" style="top:406px"><div class="name">Halibut Gumbo</div><div class="desc">Shrimp, scallions, okra garnish</div><div class="price">00</div></div>
    <div class="rule right" style="top:448px"></div>
    <div class="item" style="top:456px"><div class="name">Grilled Steak</div><div class="desc">Carrots, mashed potatoes, demi, chimichurri</div><div class="price">00</div></div>
    <div class="rule right" style="top:498px"></div>
    <div class="item" style="top:506px"><div class="name">Surf and Turf Filet</div><div class="desc">Asparagus, baby potatoes, bearnaise, demi</div><div class="price">00</div></div>

    <h2 class="heading" style="left:841px;top:562px">Handhelds</h2>
    <div class="item" style="top:608px"><div class="name">Baja Fish Tacos</div><div class="desc">Slaw, cilantro, lime</div><div class="price">00</div></div>
    <div class="item" style="top:649px"><div class="name">Steak Taco</div><div class="desc">Dried chili salsa, pickled onion, cotija</div><div class="price">00</div></div>
    <div class="item" style="top:690px"><div class="name">Fried Oyster Taco</div><div class="desc">Pickled onion, scallions, jalapeño, romesco</div><div class="price">00</div></div>
    <div class="item" style="top:731px"><div class="name">Smash Burger</div><div class="desc">Spicy mayo, pickles, house cut fries, LTO</div><div class="price">00</div></div>
    <div class="item" style="top:771px"><div class="name">Lobster Roll</div><div class="desc">House cut fries</div><div class="price">00</div></div>
    <div class="item" style="top:812px"><div class="name">Fish Sandwich</div><div class="desc">Halibut, pickled carrots, House aioli</div><div class="price">00</div></div>
  </section>

  <p class="disclaimer">Consuming raw or undercooked meats, poultry, seafood, shellfish, or eggs may increase your risk of foodborne illness</p>
</main>
</body>
</html>
```